Korvix App Graphics Design

Our application promotes location based self expression via pictures and text. The primary focus of the application is on the content posted and not on the person that posted it.

We want a very clean and fresh design that evokes positive energy. Our site is unique so our design should be as well. People will reveal thoughts on our site, so the design should convey a "revealing" feel. Our site is a place where people are comfortable to freely express themselves. Colors we have in mind are blue and green hues with earth tones for background.

Our project is to design ten screens for our Korvix application at resolution of 1136-by-640 pixels:

Feed Screen
Camera Screen
Post Screen
Check In Screen
Approval Screen
Map Screen
Flag Screen
Feed Select Screen
Export Screen
Menu Screen

In the contest phase we will require only three screens to be submitted. The screens we require to be submitted are: Feed Screen; Map Screen and Camera Screen. The designer we select as the winner of the competition will then complete the project and deliver a total of the ten screens described above in the handover phase.

We have attached a document below with detailed specs of each screen, we ask for your innovation to bring these screens to life through your design.
Updates

We want to clarify one aspect regarding the VISOR: the visor needs to be transparent so that when the picture scrolls underneath it, you can still see the picture underneath the visor.

Hi Everyone,

We have noticed that some designers need clarification regarding the visor element in the feed screen.
I have attached two examples to our brief area called:
Visor Example 1 and Visor Example 2

Please note that these are not the style we are looking for but are a good example to the concept of a Transparent Visor above the feed stream. We are looking for you guys to come up with a Visor concept that is consistent with the style of the design you are submitting.

Thanks,

Bo

Target Market(s)

People 17-40 who want to share their thought about the world around them.

Industry/Entity Type

Flag

Font styles to use
Sans Serif
Other font styles liked:
• We like “Helvetica New” or “Avenir” but are flexible

Requirements
Must have
• Visor component should look innovative.

```html
<!DOCTYPE html>
<html lang="en">
<head>
<meta charset="utf-8">
<title>Korvix App Screens</title>
<link rel="stylesheet" href="https://fonts.googleapis.com/css2?family=Nunito+Sans:wght@400;600;700&display=swap">
<style>
:root{
  --teal:#2ba4be;
  --teal-dark:#2a8ea4;
  --visor:rgba(38,128,148,.92);
  --paper:#f6f3ec;
  --earth:#e6e0d4;
  --ink:#3b3b3b;
  --muted:#8d8d8d;
  --green:#8cc63f;
  --orange:#f07a12;
  --badge:#e8413c;
  --stage:#dcdcdc;
  --caption:#555;
}
*{box-sizing:border-box;margin:0;padding:0}
html,body{width:1200px;height:1000px;overflow:hidden}
body{
  background:linear-gradient(180deg,#e6e6e6 0%,#d3d3d3 100%);
  font-family:"Nunito Sans","Helvetica Neue",Arial,sans-serif;
  color:var(--ink);
  position:relative;
}
.screen{position:absolute;top:168px;width:301px;height:534px;overflow:hidden;background:var(--earth)}
.screen--feed{left:64px}
.screen--map{left:452px;background:var(--paper)}
.screen--camera{left:839px;background:#111}
.status-bar{position:absolute;left:0;top:0;width:100%;height:20px;background:var(--teal);color:#fff;font-size:11px;display:flex;align-items:center;justify-content:space-between;padding:0 8px;z-index:3}
.status-bar .time{position:absolute;left:0;right:0;text-align:center;font-weight:600}
.nav-bar{position:absolute;left:0;top:20px;width:100%;height:42px;background:var(--teal);color:#fff;z-index:3}
.nav-bar .title{position:absolute;left:0;right:0;top:11px;text-align:center;font-size:15px}
.menu-btn{position:absolute;left:12px;top:12px}
.menu-badge{position:absolute;left:25px;top:3px;width:16px;height:12px;border-radius:6px;background:var(--badge);font-size:8px;line-height:12px;text-align:center;color:#fff}
.search-btn{position:absolute;right:12px;top:9px}
.visor{position:absolute;left:0;top:62px;width:100%;height:42px;background:var(--visor);color:#fff;text-align:center;font-size:15px;line-height:42px;z-index:2;box-shadow:0 2px 4px rgba(0,0,0,.15)}
.post{position:absolute;left:12px;width:278px;background:var(--paper);box-shadow:0 1px 2px rgba(0,0,0,.12)}
.post-head{height:50px;position:relative}
.avatar{position:absolute;left:8px;top:5px;width:40px;height:40px;border-radius:50%;border:2px solid #fff;box-shadow:0 0 0 1px #ddd}
.post-name{position:absolute;left:58px;top:8px;font-size:13.5px}
.post-place{position:absolute;left:58px;top:27px;font-size:11px;color:var(--muted)}
.post-meta{position:absolute;right:8px;top:9px;font-size:11px;color:var(--muted);text-align:right;line-height:17px}
.post-photo{position:absolute;left:-6px;width:290px;border:4px solid #fff;box-shadow:0 1px 3px rgba(0,0,0,.2)}
.photo-sunset{background:linear-gradient(180deg,#3c5a6c 0%,#c9724a 35%,#f29a3f 50%,#2a2f36 56%,#1b2229 100%)}
.photo-sky{background:linear-gradient(180deg,#7fa6c4 0%,#bcd3e3 60%,#5b6f82 100%)}
.avatar-a{background:linear-gradient(135deg,#4a3a32,#b08a72)}
.avatar-b{background:linear-gradient(135deg,#c9d4da,#8aa0ad)}
.post-actions{position:absolute;left:0;width:100%;height:40px}
.icon-circle{position:absolute;top:7px;width:27px;height:27px;border-radius:50%;background:#bdbdbd;display:flex;align-items:center;justify-content:center}
.score{position:absolute;left:122px;top:-18px;width:36px;height:40px}
.fab{position:absolute;top:476px;width:50px;height:50px;border-radius:50%;background:var(--teal);border:2px solid #fff;display:flex;align-items:center;justify-content:center;box-shadow:0 1px 4px rgba(0,0,0,.3);z-index:4}
.place-list{position:absolute;top:62px;left:0;width:100%}
.place{height:41px;border-bottom:1px solid #e2ddd2;position:relative;background:var(--paper)}
.place-thumb{position:absolute;left:10px;top:3px;width:35px;height:35px;background:#ece6d6;border:1px solid #d8d2c4}
.place-name{position:absolute;left:56px;top:10px;font-size:15px}
.place-dist{position:absolute;right:24px;top:12px;font-size:11px;color:var(--green);font-style:italic}
.chev{position:absolute;right:10px;top:14px}
.map-search{position:absolute;left:6px;top:232px;width:289px;height:26px;border-radius:5px;background:#e4e4e4;font-size:11px;color:#9a9a9a;font-style:italic;padding:6px 0 0 26px}
.map-search svg{position:absolute;left:8px;top:6px}
.map-area{position:absolute;left:0;top:262px;width:100%;height:272px;background:linear-gradient(160deg,#f4f0e4 0%,#efe9da 60%,#f2e8c8 100%)}
.map-overlay{position:absolute;left:0;top:262px}
.cam-photo{position:absolute;inset:0;background:linear-gradient(150deg,#b5a27a 0%,#d9c99e 40%,#ece0bd 60%,#a08b66 100%)}
.cam-top{position:absolute;top:10px;width:34px;height:34px;border-radius:50%;background:rgba(43,164,190,.85);display:flex;align-items:center;justify-content:center}
.effects{position:absolute;left:0;top:400px;width:100%;height:66px;background:rgba(30,30,30,.78)}
.effect{position:absolute;top:4px;width:44px;text-align:center;font-size:9.5px;color:#fff;font-style:italic}
.effect span{display:block;width:44px;height:44px;border-radius:50%;border:2px solid #fff;background:linear-gradient(135deg,#3f6f8a,#d8c8a4);margin-bottom:2px}
.cam-tools{position:absolute;left:0;top:466px;width:100%;height:68px;background:#151515}
.tool{position:absolute;top:22px}
.shutter{position:absolute;left:124px;top:8px;width:52px;height:52px;border-radius:50%;background:var(--teal);display:flex;align-items:center;justify-content:center}
.caption{position:absolute;left:72px;top:874px;font-size:32px;line-height:41px;color:var(--caption);font-weight:400;letter-spacing:.2px}
.caption strong{font-weight:700}
</style>
</head>
<body>

<!-- Feed screen -->
<section class="screen screen--feed">
  <div class="status-bar"><span>●●●●○ Carrier</span><span class="time">4:20 AM</span><span>100% ▭</span></div>
  <header class="nav-bar">
    <svg class="menu-btn" width="22" height="18" viewBox="0 0 22 18"><g stroke="#fff" stroke-width="2"><line x1="0" y1="2" x2="22" y2="2"/><line x1="0" y1="9" x2="22" y2="9"/><line x1="0" y1="16" x2="22" y2="16"/></g></svg>
    <span class="menu-badge">23</span>
    <div class="title">Feed Name ▸</div>
    <svg class="search-btn" width="22" height="22" viewBox="0 0 22 22"><circle cx="9" cy="9" r="7" fill="none" stroke="#fff" stroke-width="2"/><line x1="14" y1="14" x2="21" y2="21" stroke="#fff" stroke-width="2.2"/></svg>
  </header>
  <div class="visor">Lets Go to The Beach</div>

  <article class="post" style="top:112px;height:285px">
    <div class="post-head">
      <div class="avatar avatar-a" role="img" aria-label="Profile photo of the poster"></div>
      <div class="post-name">Mira Dawn</div>
      <div class="post-place"><span style="color:var(--green)">⚲</span> Los Angeles, CA</div>
      <div class="post-meta"><span style="color:var(--green)">◷</span> 2 mins<br><span style="color:var(--green)">➚</span> 0.1 mi</div>
    </div>
    <div class="post-photo photo-sunset" style="top:50px;height:194px" role="img" aria-label="Photo of a woman on a pier at sunset over the sea"></div>
    <div class="post-actions" style="top:245px">
      <span class="icon-circle" style="left:10px"><svg width="15" height="12" viewBox="0 0 15 12"><path d="M1 4h3l6-3v10L4 8H1z" fill="#fff"/></svg></span>
      <span class="icon-circle" style="left:64px"><svg width="15" height="12" viewBox="0 0 15 12"><path d="M1 4h3l6-3v10L4 8H1z" fill="#fff"/><path d="M12 3q2 3 0 6" stroke="#fff" fill="none"/></svg></span>
      <svg class="score" viewBox="0 0 36 40"><polygon points="18,1 35,10 35,30 18,39 1,30 1,10" fill="var(--orange)" stroke="#fff" stroke-width="1.5"/><text x="18" y="25" text-anchor="middle" fill="#fff" font-size="15" font-family="Nunito Sans, sans-serif">20</text></svg>
      <svg style="position:absolute;left:204px;top:9px" width="22" height="22" viewBox="0 0 22 22"><path d="M3 21L8 3M8 3l11 4-5 4 3 6-11-4" stroke="#888" stroke-width="1.5" fill="none"/></svg>
      <svg style="position:absolute;left:248px;top:9px" width="24" height="20" viewBox="0 0 24 20"><path d="M14 2l8 7-8 7v-4C8 12 4 14 2 18c0-7 4-11 12-11z" stroke="#888" stroke-width="1.5" fill="none"/></svg>
    </div>
  </article>

  <article class="post" style="top:404px;height:150px">
    <div class="post-head">
      <div class="avatar avatar-b" role="img" aria-label="Profile photo of the poster"></div>
      <div class="post-name">Lena Brooks</div>
      <div class="post-place"><span style="color:var(--green)">⚲</span> Los Angeles, CA</div>
      <div class="post-meta"><span style="color:var(--green)">◷</span> 10 mins<br><span style="color:var(--green)">➚</span> 0.1 mi</div>
    </div>
    <div class="post-photo photo-sky" style="top:50px;height:100px" role="img" aria-label="Photo of a person against a hazy sky"></div>
  </article>

  <span class="fab" style="left:12px"><svg width="24" height="20" viewBox="0 0 24 20"><rect x="1" y="4" width="22" height="15" rx="3" fill="none" stroke="#fff" stroke-width="2"/><circle cx="12" cy="11.5" r="4.5" fill="none" stroke="#fff" stroke-width="2"/><rect x="8" y="1" width="8" height="3" fill="#fff"/></svg></span>
  <span class="fab" style="left:240px"><svg width="22" height="22" viewBox="0 0 22 22"><path d="M6 2h10v6a5 5 0 0 1-10 0z M6 4H2q0 5 4 6 M16 4h4q0 5-4 6 M11 13v4 M7 20h8" stroke="#fff" stroke-width="1.8" fill="none"/></svg></span>
</section>

<!-- Map screen -->
<section class="screen screen--map">
  <div class="status-bar"><span>●●●●○ Carrier</span><span class="time">4:20 AM</span><span>100% ▭</span></div>
  <header class="nav-bar">
    <svg class="menu-btn" width="22" height="18" viewBox="0 0 22 18"><g stroke="#fff" stroke-width="2"><line x1="0" y1="2" x2="22" y2="2"/><line x1="0" y1="9" x2="22" y2="9"/><line x1="0" y1="16" x2="22" y2="16"/></g></svg>
    <span class="menu-badge">23</span>
    <div class="title">Map</div>
  </header>
  <ul class="place-list" style="list-style:none">
    <li class="place"><span class="place-thumb" role="img" aria-label="Map thumbnail"></span><span class="place-name">Art Street</span><span class="place-dist">➚0.1mi</span><svg class="chev" width="7" height="12"><path d="M1 1l5 5-5 5" stroke="#aaa" fill="none" stroke-width="1.5"/></svg></li>
    <li class="place"><span class="place-thumb" role="img" aria-label="Map thumbnail"></span><span class="place-name">Landscpe Viewer</span><span class="place-dist">➚0.2mi</span><svg class="chev" width="7" height="12"><path d="M1 1l5 5-5 5" stroke="#aaa" fill="none" stroke-width="1.5"/></svg></li>
    <li class="place"><span class="place-thumb" role="img" aria-label="Map thumbnail"></span><span class="place-name">High Building</span><span class="place-dist">➚0.3mi</span><svg class="chev" width="7" height="12"><path d="M1 1l5 5-5 5" stroke="#aaa" fill="none" stroke-width="1.5"/></svg></li>
    <li class="place"><span class="place-thumb" role="img" aria-label="Map thumbnail"></span><span class="place-name">Lorem Ipsum</span><span class="place-dist">➚0.4mi</span><svg class="chev" width="7" height="12"><path d="M1 1l5 5-5 5" stroke="#aaa" fill="none" stroke-width="1.5"/></svg></li>
  </ul>
  <div class="map-search"><svg width="13" height="13" viewBox="0 0 13 13"><circle cx="7.5" cy="5.5" r="4.5" fill="none" stroke="#999"/><line x1="4.5" y1="8.5" x2="1" y2="12" stroke="#999" stroke-width="1.4"/></svg>Search here</div>
  <div class="map-area" role="img" aria-label="Street map of the surrounding neighbourhood"></div>
  <svg class="map-overlay" width="301" height="272" viewBox="0 0 301 272">
    <circle cx="152" cy="118" r="78" fill="rgba(43,164,190,.15)" stroke="var(--teal)" stroke-width="1.5"/>
    <g fill="var(--teal)" stroke="#555" stroke-width="1">
      <line x1="100" y1="30" x2="100" y2="46"/><circle cx="100" cy="28" r="6"/>
      <line x1="41" y1="48" x2="41" y2="66"/><circle cx="41" cy="46" r="6"/>
      <line x1="53" y1="110" x2="53" y2="126"/><circle cx="53" cy="108" r="6"/>
      <line x1="149" y1="104" x2="149" y2="120"/><circle cx="149" cy="102" r="6"/>
      <line x1="249" y1="16" x2="249" y2="34"/><circle cx="249" cy="14" r="6"/>
    </g>
    <circle cx="219" cy="84" r="10" fill="var(--teal)" stroke="#fff" stroke-width="2"/>
  </svg>
  <span class="fab" style="left:12px;top:482px;width:40px;height:40px"><svg width="18" height="18" viewBox="0 0 18 18"><path d="M17 1L1 8l7 2 2 7z" fill="none" stroke="#fff" stroke-width="1.8"/></svg></span>
  <span class="fab" style="left:249px;top:482px;width:40px;height:40px"><svg width="14" height="22" viewBox="0 0 14 22"><circle cx="7" cy="6" r="5" fill="none" stroke="#fff" stroke-width="1.8"/><line x1="7" y1="11" x2="7" y2="21" stroke="#fff" stroke-width="1.8"/></svg></span>
</section>

<!-- Camera screen -->
<section class="screen screen--camera">
  <div class="cam-photo" role="img" aria-label="Camera preview of a woman in sunglasses holding a shoulder bag"></div>
  <span class="cam-top" style="left:18px"><svg width="18" height="15" viewBox="0 0 18 15"><rect x="1" y="3" width="16" height="11" rx="2" fill="none" stroke="#fff" stroke-width="1.5"/><path d="M6 9a3 3 0 0 1 6-1M12 8a3 3 0 0 1-6 1" stroke="#fff" fill="none"/></svg></span>
  <span class="cam-top" style="left:96px"><svg width="12" height="18" viewBox="0 0 12 18"><path d="M8 1L2 10h4l-2 7 7-10H7z" fill="none" stroke="#fff" stroke-width="1.4"/></svg></span>
  <span class="cam-top" style="left:172px"><svg width="20" height="20" viewBox="0 0 20 20"><circle cx="10" cy="10" r="7" fill="none" stroke="#fff" stroke-width="1.5"/><path d="M10 0v6M10 14v6M0 10h6M14 10h6" stroke="#fff" stroke-width="1.5"/></svg></span>
  <span class="cam-top" style="left:248px"><svg width="14" height="14" viewBox="0 0 14 14"><path d="M1 1l12 12M13 1L1 13" stroke="#fff" stroke-width="2"/></svg></span>
  <div class="effects">
    <div class="effect" style="left:10px"><span role="img" aria-label="Filter preview"></span>Effect 1</div>
    <div class="effect" style="left:69px"><span role="img" aria-label="Filter preview"></span>Effect 2</div>
    <div class="effect" style="left:129px"><span role="img" aria-label="Filter preview"></span>Effect 3</div>
    <div class="effect" style="left:189px"><span role="img" aria-label="Filter preview"></span>Effect 4</div>
    <div class="effect" style="left:248px"><span role="img" aria-label="Filter preview"></span>Effect 5</div>
  </div>
  <div class="cam-tools">
    <svg class="tool" style="left:22px" width="22" height="22" viewBox="0 0 22 22"><path d="M4 9a7 7 0 0 1 13-2M18 13a7 7 0 0 1-13 2" stroke="#fff" stroke-width="2" fill="none"/><path d="M17 2v5h-5M5 20v-5h5" stroke="#fff" stroke-width="2" fill="none"/></svg>
    <svg class="tool" style="left:70px" width="22" height="22" viewBox="0 0 22 22"><circle cx="11" cy="11" r="4" fill="#fff"/><g stroke="#fff" stroke-width="2"><path d="M11 0v4M11 18v4M0 11h4M18 11h4M3 3l3 3M16 16l3 3M19 3l-3 3M6 16l-3 3"/></g></svg>
    <span class="shutter"><svg width="24" height="20" viewBox="0 0 24 20"><rect x="1" y="4" width="22" height="15" rx="3" fill="#fff"/><circle cx="12" cy="11.5" r="4.5" fill="var(--teal)"/><rect x="8" y="1" width="8" height="4" fill="#fff"/></svg></span>
    <svg class="tool" style="left:206px" width="22" height="22" viewBox="0 0 22 22"><path d="M5 0v17h17M0 5h17v17" stroke="#fff" stroke-width="2" fill="none"/><path d="M4 18L18 4" stroke="#fff" stroke-width="1.5"/></svg>
    <svg class="tool" style="left:256px" width="22" height="22" viewBox="0 0 22 22"><path d="M2 20L15 7" stroke="var(--teal)" stroke-width="3"/><path d="M17 1v4M15 3h4M20 8v3M19 9.5h2" stroke="#fff" stroke-width="1.3"/></svg>
  </div>
</section>

<p class="caption">Be sure to check the <strong>UX animation</strong> video<br>and let me know what you think</p>

</body>
</html>
```